Business card and stationary for a garage
Motorwerkplaats Lindeveld
@ph - changes done .Please check and confirm.- Thanks
@quickdraft
Can you please make another version with #136 as the front and #135 as the back side.
Note 1: Please omit the word "Services" and make the logo a little bit bigger at the back side
Note 2: It's Merelhoflaan
Note 3: #135 the back side. The text "Motorwerkplaats Lindeveld" is too gray. Just use the original logo and colors.
#ALL
Please use "T" for phonenumber and "F" for fax. Do not use the English abbreviations. Or better use icons.
Nice designs, thank you.
We dont prefer a style like #124-#129 for the back of the card. Its to simple. The service listing can be more attractive like in #121 or #118 (horizontal).
#ALL please do not use english words in business card like "Our services". Use only "Services" as this is also a common word in Dutch.
"Voor alle merken" means "For all brands"

```html
<!DOCTYPE html>
<html lang="nl">
<head>
<meta charset="utf-8">
<title>Motorwerkplaats Lindeveld – huisstijl</title>
<link href="https://fonts.googleapis.com/css2?family=Archivo:wght@400;700&display=swap" rel="stylesheet">
<style>
  :root {
    --page-bg: #ffffff;
    --frame: #e2e2e2;
    --paper: #ffffff;
    --red: #c8102e;
    --ink: #2b2b2b;
    --rule: #b5b5b5;
    --shadow: rgba(0,0,0,0.28);
  }
  * { margin: 0; padding: 0; box-sizing: border-box; }
  html, body { width: 1200px; height: 681px; overflow: hidden; background: var(--page-bg); }
  body { position: relative; font-family: "Archivo", Arial, sans-serif; color: var(--ink); }
  .presentation-frame {
    position: absolute; left: 24px; top: 22px; width: 1152px; height: 626px;
    border: 2px solid var(--frame);
  }
  .sheet {
    position: absolute; background: var(--paper); overflow: hidden;
    box-shadow: 4px 5px 10px var(--shadow);
  }
  .top-band { position: absolute; left: 0; top: 0; width: 100%; background: var(--red); }
  .top-rule { position: absolute; left: 0; width: 100%; height: 1px; background: var(--rule); }
  .brand {
    position: absolute; font-weight: 700; color: var(--red);
    letter-spacing: 0.02em; white-space: nowrap; text-transform: uppercase;
  }
  .small-text { position: absolute; color: var(--ink); white-space: nowrap; }

  .envelope-front { left: 44px; top: 96px; width: 508px; height: 204px; }
  .envelope-front .top-band { height: 6px; }
  .envelope-front .top-rule { top: 11px; }
  .envelope-front .brand { left: 26px; top: 62px; font-size: 12px; }
  .envelope-front .small-text { left: 26px; top: 96px; font-size: 7px; }

  .envelope-back { left: 44px; top: 360px; width: 508px; height: 212px; }
  .envelope-back .flap { position: absolute; left: 0; top: 0; width: 100%; height: 40px; }
  .envelope-back .brand { left: 0; right: 0; top: 44px; text-align: center; font-size: 12px; }

  .letterhead { left: 618px; top: 48px; width: 312px; height: 576px; }
  .letterhead .top-band { height: 5px; }
  .letterhead .top-rule { top: 9px; }
  .letterhead .brand { left: 24px; top: 56px; font-size: 9px; }
  .letterhead .contact { left: 24px; top: 84px; font-size: 5px; line-height: 7.5px; }

  .card { width: 166px; height: 106px; }
  .card-front { left: 965px; top: 134px; }
  .card-back { left: 965px; top: 266px; }
  .card .top-band { height: 4px; }
  .card .top-rule { top: 7px; }
  .card-front .brand { left: 10px; top: 42px; font-size: 6px; }
  .card-front .person { left: 100px; top: 28px; font-size: 5px; font-weight: 700; }
  .card-front .details { left: 100px; top: 46px; font-size: 3.5px; line-height: 5.5px; }
  .card-back .brand { left: 0; right: 0; top: 30px; text-align: center; font-size: 7px; }
  .card-back .services { left: 0; right: 0; top: 72px; text-align: center; font-size: 4px; line-height: 6px; }
</style>
</head>
<body>
<div class="presentation-frame"></div>

<section class="sheet envelope-front" aria-label="Envelop voorzijde">
  <div class="top-band"></div><div class="top-rule"></div>
  <div class="brand">Motorwerkplaats Lindeveld</div>
  <div class="small-text">Merelhoflaan 41 · 3704 GE Lindeveld</div>
</section>

<section class="sheet envelope-back" aria-label="Envelop achterzijde">
  <svg class="flap" viewBox="0 0 508 40" preserveAspectRatio="none">
    <path d="M0 0 L10 30 L498 30 L508 0" stroke="var(--rule)" stroke-width="1" fill="none"/>
  </svg>
  <div class="brand">Motorwerkplaats Lindeveld</div>
</section>

<section class="sheet letterhead" aria-label="Briefpapier">
  <div class="top-band"></div><div class="top-rule"></div>
  <div class="brand">Motorwerkplaats Lindeveld</div>
  <div class="small-text contact">
    Merelhoflaan 41<br>3704 GE Lindeveld<br>T 030 123 45 67<br>F 030 123 45 68<br>E info@bolwerkxq.nl<br>W www.bolwerkxq.nl
  </div>
</section>

<section class="sheet card card-front" aria-label="Visitekaartje voorzijde">
  <div class="top-band"></div><div class="top-rule"></div>
  <div class="brand">Lindeveld</div>
  <div class="small-text person">Ruud Verbeek</div>
  <div class="small-text details">Merelhoflaan 41<br>3704 GE Lindeveld<br>T 030 123 45 67<br>F 030 123 45 68<br>info@bolwerkxq.nl</div>
</section>

<section class="sheet card card-back" aria-label="Visitekaartje achterzijde">
  <div class="top-band"></div><div class="top-rule"></div>
  <div class="brand">Lindeveld</div>
  <div class="small-text services">APK · Onderhoud · Banden<br>Voor alle merken</div>
</section>
</body>
</html>
```